Need Powerpoint masters for my consulting company in privacy (RGPD) and IT

For my newly created consulting company I need powerpoint slides masters.
The company is specialzed in privacy (RGPD) and IT.
The company already has a logo (obtained via Marquelane).
These master slides will be mainly used when presenting reports/analysis to clients.
I'll attach a PNG files of the logo.

```html
<!DOCTYPE html>
<html lang="en">
<head>
<meta charset="utf-8">
<title>Adrien Valcourt – Presentation Masters</title>
<link href="https://fonts.googleapis.com/css2?family=Poppins:wght@300;400;500;600;700&family=Open+Sans:wght@400;600&display=swap" rel="stylesheet">
<style>
:root{
  --teal:#0e8a99;
  --teal-deep:#0b6577;
  --navy:#0d3a4f;
  --ink:#1b2a33;
  --grey:#555a5e;
  --light:#eef2f3;
  --white:#ffffff;
  --stage:#000000;
  --hero-top:#c9cfd3;
  --hero-bottom:#e4e2de;
}
*{margin:0;padding:0;box-sizing:border-box}
html,body{width:1200px;height:3405px;overflow:hidden;background:var(--stage)}
.sheet{position:relative;width:1200px;height:3405px;background:var(--stage)}
.hero{position:absolute;left:0;top:0;width:1200px;height:700px;background:linear-gradient(180deg,var(--hero-top),var(--hero-bottom) 80%,var(--stage))}
.hero-slide{position:absolute;left:190px;top:110px;width:680px;height:382px;box-shadow:0 20px 40px rgba(0,0,0,.25)}
.hero-brand{position:absolute;left:860px;top:120px;font-family:'Poppins',sans-serif;font-weight:500;font-size:26px;color:var(--teal)}
.slide{position:absolute;width:563px;height:316px;overflow:hidden;background:var(--white)}
.slide svg{display:block;width:100%;height:100%}
.c1{left:28px}.c2{left:609px}.cc{left:318px}
.r1{top:714px}.r2{top:1048px}.r3{top:1384px}.r4{top:1718px}.r5{top:2052px}.r6{top:2388px}.r7{top:2722px}.r8{top:3057px}
.h{font-family:'Poppins',sans-serif;font-weight:700}
.hl{font-family:'Poppins',sans-serif;font-weight:300}
.hm{font-family:'Poppins',sans-serif;font-weight:500}
.b{font-family:'Open Sans',sans-serif;font-weight:400}
.bs{font-family:'Open Sans',sans-serif;font-weight:600}
.brand{font-family:'Poppins',sans-serif;font-weight:500}
</style>
</head>
<body>
<div class="sheet">

<section class="hero">
  <div class="hero-slide">
    <svg viewBox="0 0 563 316">
      <defs><linearGradient id="gTeal" x1="0" y1="0" x2="1" y2="1"><stop offset="0" stop-color="#0e7d8d"/><stop offset="1" stop-color="#0a4f63"/></linearGradient></defs>
      <rect width="563" height="316" fill="#fff"/>
      <path d="M0 0H563V193H405L370 232H0Z" fill="url(#gTeal)" role="img" aria-label="Photo of a team meeting around a table, tinted teal"/>
      <path d="M0 232H370L405 193H563V197H408L373 236H0Z" fill="var(--navy)"/>
      <text class="h" x="44" y="72" font-size="33" fill="#fff">Presentation</text>
      <text class="h" x="44" y="106" font-size="33" fill="#fff">Title Goes Here!</text>
      <text class="b" x="44" y="132" font-size="15" fill="#fff">Subtitle of Presentation Goes Here!</text>
      <text class="b" x="44" y="182" font-size="8" fill="#fff">Thursday, October 14, 2021</text>
      <text class="brand" x="470" y="280" font-size="15" fill="var(--teal)" text-anchor="middle">Adrien Valcourt</text>
    </svg>
  </div>
  <div class="hero-brand">Adrien Valcourt</div>
</section>

<!-- Title master 1 -->
<div class="slide c1 r1"><svg viewBox="0 0 563 316">
  <defs><linearGradient id="t1" x1="0" y1="0" x2="1" y2="1"><stop offset="0" stop-color="#0e7d8d"/><stop offset="1" stop-color="#0a4f63"/></linearGradient></defs>
  <path d="M0 0H563V193H405L370 232H0Z" fill="url(#t1)" role="img" aria-label="Photo of a team meeting, tinted teal"/>
  <path d="M0 232H370L405 193H563V197H408L373 236H0Z" fill="var(--navy)"/>
  <text class="h" x="44" y="72" font-size="33" fill="#fff">Presentation</text>
  <text class="h" x="44" y="106" font-size="33" fill="#fff">Title Goes Here!</text>
  <text class="b" x="44" y="132" font-size="15" fill="#fff">Subtitle of Presentation Goes Here!</text>
  <text class="b" x="44" y="182" font-size="8" fill="#fff">Thursday, October 14, 2021</text>
  <text class="brand" x="455" y="280" font-size="15" fill="var(--teal)" text-anchor="middle">Adrien Valcourt</text>
</svg></div>

<!-- Title master 2 -->
<div class="slide c2 r1"><svg viewBox="0 0 563 316">
  <defs><linearGradient id="t2" x1="0" y1="0" x2="1" y2="0"><stop offset="0" stop-color="#f7f8f8"/><stop offset="1" stop-color="#dfe5e7"/></linearGradient>
  <linearGradient id="t2b" x1="0" y1="0" x2="1" y2="0"><stop offset="0" stop-color="#0e8a99"/><stop offset="1" stop-color="#0d3a4f"/></linearGradient></defs>
  <rect width="563" height="316" fill="url(#t2)" role="img" aria-label="Faded photo of hands using a tablet"/>
  <path d="M0 232H370L405 193H563V316H0Z" fill="url(#t2b)"/>
  <path d="M0 232H370L405 193H563V197H408L373 236H0Z" fill="var(--navy)"/>
  <text class="h" x="44" y="72" font-size="33" fill="var(--navy)">Presentation</text>
  <text class="h" x="44" y="106" font-size="33" fill="var(--navy)">Title Goes Here!</text>
  <text class="b" x="44" y="132" font-size="15" fill="var(--teal)">Subtitle of Presentation Goes Here!</text>
  <text class="b" x="44" y="182" font-size="8" fill="#999">Thursday, October 14, 2021</text>
  <text class="brand" x="455" y="280" font-size="15" fill="#fff" text-anchor="middle">Adrien Valcourt</text>
</svg></div>

<!-- Title master 3 -->
<div class="slide c1 r2"><svg viewBox="0 0 563 316">
  <defs><linearGradient id="t3" x1="0" y1="0" x2="1" y2="1"><stop offset="0" stop-color="#0a5a6c"/><stop offset="1" stop-color="#10909e"/></linearGradient></defs>
  <path d="M0 0H563V193H405L370 232H0Z" fill="url(#t3)" role="img" aria-label="Photo of a report with charts, tinted teal"/>
  <path d="M0 232H370L405 193H563V197H408L373 236H0Z" fill="var(--navy)"/>
  <text class="h" x="44" y="72" font-size="33" fill="var(--navy)">Presentation</text>
  <text class="h" x="44" y="106" font-size="33" fill="var(--navy)">Title Goes Here!</text>
  <text class="b" x="44" y="132" font-size="15" fill="var(--navy)">Subtitle of Presentation Goes Here!</text>
  <text class="b" x="44" y="182" font-size="8" fill="#fff">Thursday, October 14, 2021</text>
  <text class="brand" x="455" y="280" font-size="15" fill="var(--teal)" text-anchor="middle">Adrien Valcourt</text>
</svg></div>

<!-- Title master 4 -->
<div class="slide c2 r2"><svg viewBox="0 0 563 316">
  <defs><linearGradient id="t4" x1="0" y1="0" x2="1" y2="1"><stop offset="0" stop-color="#f5f6f6"/><stop offset="1" stop-color="#e2e6e7"/></linearGradient></defs>
  <rect width="563" height="316" fill="url(#t4)" role="img" aria-label="Faded overhead photo of a desk with laptop"/>
  <path d="M0 232H340L375 193H563V316H0Z" fill="var(--navy)"/>
  <path d="M0 232H340L375 193H563V197H378L343 236H0Z" fill="var(--teal)"/>
  <text class="h" x="44" y="72" font-size="33" fill="var(--navy)">Presentation</text>
  <text class="h" x="44" y="106" font-size="33" fill="var(--navy)">Title Goes Here!</text>
  <text class="b" x="44" y="132" font-size="15" fill="var(--teal)">Subtitle of Presentation Goes Here!</text>
  <text class="b" x="44" y="182" font-size="8" fill="#999">Thursday, October 14, 2021</text>
  <text class="brand" x="455" y="280" font-size="15" fill="#fff" text-anchor="middle">Adrien Valcourt</text>
</svg></div>

<!-- Title master 5 -->
<div class="slide c1 r3"><svg viewBox="0 0 563 316">
  <defs><linearGradient id="t5" x1="0" y1="0" x2="1" y2="1"><stop offset="0" stop-color="#f6f7f7"/><stop offset="1" stop-color="#dde3e4"/></linearGradient></defs>
  <rect width="563" height="316" fill="url(#t5)" role="img" aria-label="Faded photo of a team meeting"/>
  <path d="M0 232H370L405 193H563V316H0Z" fill="var(--teal)"/>
  <path d="M0 232H370L405 193H563V197H408L373 236H0Z" fill="var(--navy)"/>
  <text class="h" x="44" y="72" font-size="33" fill="var(--navy)">Presentation</text>
  <text class="h" x="44" y="106" font-size="33" fill="var(--navy)">Title Goes Here!</text>
  <text class="b" x="44" y="132" font-size="15" fill="var(--teal)">Subtitle of Presentation Goes Here!</text>
  <text class="b" x="44" y="182" font-size="8" fill="#999">Thursday, October 14, 2021</text>
  <text class="brand" x="455" y="280" font-size="15" fill="#fff" text-anchor="middle">Adrien Valcourt</text>
</svg></div>

<!-- Table of content -->
<div class="slide c2 r3"><svg viewBox="0 0 563 316">
  <text class="hl" x="33" y="48" font-size="22" fill="var(--teal)">Table of <tspan class="hm">Content</tspan></text>
  <line x1="33" y1="58" x2="230" y2="58" stroke="var(--teal)" stroke-width="1"/>
  <g class="hl" font-size="20" fill="#aab">
    <text x="75" y="122">1</text><text x="297" y="122">2</text>
    <text x="75" y="177">3</text><text x="297" y="177">4</text>
    <text x="75" y="232">5</text><text x="297" y="232">6</text>
  </g>
  <g class="hm" font-size="12" fill="var(--teal)">
    <text x="107" y="110">Title <tspan class="hl">Goes Here!</tspan></text><text x="329" y="110">Title <tspan class="hl">Goes Here!</tspan></text>
    <text x="107" y="165">Title <tspan class="hl">Goes Here!</tspan></text><text x="329" y="165">Title <tspan class="hl">Goes Here!</tspan></text>
    <text x="107" y="220">Title <tspan class="hl">Goes Here!</tspan></text><text x="329" y="220">Title <tspan class="hl">Goes Here!</tspan></text>
  </g>
  <g class="b" font-size="6.5" fill="#555">
    <text x="107" y="121">Lorem ipsum dolor sit amet, consectetur</text><text x="107" y="129">adipiscing elit. Vivamus eu dui ex.</text>
    <text x="329" y="121">Lorem ipsum dolor sit amet, consectetur</text><text x="329" y="129">adipiscing elit. Vivamus eu dui ex.</text>
    <text x="107" y="176">Lorem ipsum dolor sit amet, consectetur</text><text x="107" y="184">adipiscing elit. Vivamus eu dui ex.</text>
    <text x="329" y="176">Lorem ipsum dolor sit amet, consectetur</text><text x="329" y="184">adipiscing elit. Vivamus eu dui ex.</text>
    <text x="107" y="231">Lorem ipsum dolor sit amet, consectetur</text><text x="107" y="239">adipiscing elit. Vivamus eu dui ex.</text>
    <text x="329" y="231">Lorem ipsum dolor sit amet, consectetur</text><text x="329" y="239">adipiscing elit. Vivamus eu dui ex.</text>
  </g>
  <path d="M0 276H70L90 298H563V316H0Z" fill="#fff"/>
  <path d="M0 276H70L94 302H563V304H92L69 279H0Z" fill="var(--teal)"/>
  <path d="M0 304H563V316H0Z" fill="#fff"/>
  <text class="brand" x="8" y="293" font-size="7" fill="var(--teal)">Adrien Valcourt</text>
  <text class="b" x="530" y="300" font-size="4.5" fill="#444" text-anchor="end">Copyright 2021 Adrien Valcourt. All rights reserved  |</text>
  <text class="b" x="545" y="300" font-size="5" fill="#444" text-anchor="end">6</text>
</svg></div>

<!-- Content with photo -->
<div class="slide c1 r4"><svg viewBox="0 0 563 316">
  <defs><linearGradient id="p7" x1="0" y1="0" x2="1" y2="1"><stop offset="0" stop-color="#2c4a63"/><stop offset="1" stop-color="#c6d3e0"/></linearGradient></defs>
  <rect x="26" y="0" width="247" height="233" fill="url(#p7)" role="img" aria-label="Photo of business people working on a tablet"/>
  <text class="hm" x="300" y="48" font-size="22" fill="var(--teal)">Slide Title</text>
  <text class="hl" x="300" y="73" font-size="22" fill="var(--teal)">Goes Here!</text>
  <line x1="300" y1="83" x2="520" y2="83" stroke="var(--teal)" stroke-width="1"/>
  <g class="b" font-size="7.6" fill="#444">
    <text x="300" y="108">Lorem ipsum dolor sit amet, consectetur adipiscing</text>
    <text x="300" y="117">elit. Vivamus eu dui ex. Curabitur dapibus dignissim</text>
    <text x="300" y="126">dui, in molestie metus feugiat sed. Praesent aliquet</text>
    <text x="300" y="135">lorem ex, eu dapibus odio varius at. Duis eget tellus</text>
    <text x="300" y="144">porta, consequat lacus vitae, venenatis dolor.</text>
    <text x="300" y="162" font-size="6.8">Nulla facilisi. In et sollicitudin lacus. Donec risus orci, gravida</text>
    <text x="300" y="170" font-size="6.8">sit amet risus vehicula, aliquet pretium sapien. Nullam sit</text>
    <text x="300" y="178" font-size="6.8">amet magna non ex bibendum mollis. Nunc vel neque eu</text>
    <text x="300" y="186" font-size="6.8">augue dignissim congue ut vitae magna. Phasellus eget</text>
    <text x="300" y="194" font-size="6.8">commodo arcu. Nunc vitae semper dui. Integer venenatis,</text>
    <text x="300" y="202" font-size="6.8">tellus sit amet interdum pretium, erat neque rhoncus turpis,</text>
    <text x="300" y="210" font-size="6.8">a aliquam augue ligula eget erat. Nunc placerat, arcu nec</text>
    <text x="300" y="218" font-size="6.8">mattis fermentum, nisl mauris convallis nunc.</text>
  </g>
  <path d="M0 276H70L94 302H563V304H92L69 279H0Z" fill="var(--teal)"/>
  <path d="M0 279H69L92 304H0Z" fill="var(--teal)"/>
  <path d="M0 304H563V307H0Z" fill="var(--navy)"/>
  <text class="brand" x="8" y="295" font-size="7" fill="#fff">Adrien Valcourt</text>
  <text class="b" x="530" y="300" font-size="4.5" fill="#444" text-anchor="end">Copyright 2021 Adrien Valcourt. All rights reserved  |</text>
  <text class="b" x="545" y="300" font-size="5" fill="#444" text-anchor="end">7</text>
</svg></div>

<!-- Section break teal -->
<div class="slide c2 r4"><svg viewBox="0 0 563 316">
  <defs><linearGradient id="s8" x1="0" y1="0" x2="1" y2="1"><stop offset="0" stop-color="#0a5a6c"/><stop offset="0.6" stop-color="#0e8391"/><stop offset="1" stop-color="#2b9fad"/></linearGradient></defs>
  <rect width="563" height="316" fill="url(#s8)" role="img" aria-label="Photo of a financial report on a desk, tinted teal"/>
  <text class="brand" x="45" y="150" font-size="16" fill="#fff">Adrien Valcourt</text>
  <text class="h" x="45" y="210" font-size="32" fill="#fff">Section Break</text>
  <text class="b" x="45" y="240" font-size="14" fill="#fff">Subtitle of Section Break Goes Here!</text>
</svg></div>

<!-- Icons with rings -->
<div class="slide c1 r5"><svg viewBox="0 0 563 316">
  <text class="hm" x="33" y="48" font-size="22" fill="var(--teal)">Slide Title Goes Here!</text>
  <line x1="33" y1="58" x2="280" y2="58" stroke="var(--teal)" stroke-width="1"/>
  <g fill="none" stroke-width="5">
    <circle cx="104" cy="142" r="45" stroke="var(--navy)" stroke-dasharray="226 57" transform="rotate(-30 104 142)"/>
    <circle cx="222" cy="142" r="45" stroke="var(--teal)" stroke-dasharray="226 57" transform="rotate(-30 222 142)"/>
    <circle cx="340" cy="142" r="45" stroke="var(--grey)" stroke-dasharray="226 57" transform="rotate(-30 340 142)"/>
    <circle cx="458" cy="142" r="45" stroke="#111" stroke-dasharray="226 57" transform="rotate(-30 458 142)"/>
  </g>
  <circle cx="104" cy="99" r="15" fill="var(--navy)"/><circle cx="222" cy="99" r="15" fill="var(--teal)"/>
  <circle cx="340" cy="99" r="15" fill="var(--grey)"/><circle cx="458" cy="99" r="15" fill="#111"/>
  <g fill="#fff"><circle cx="104" cy="97" r="5"/><rect x="101" y="102" width="6" height="4"/>
  <path d="M216 104l10-10 2 2-10 10z"/><circle cx="340" cy="99" r="6" fill="none" stroke="#fff" stroke-width="3"/>
  <circle cx="458" cy="95" r="4"/><path d="M451 106a7 6 0 0 1 14 0z"/></g>
  <g class="bs" font-size="8" text-anchor="middle">
    <text x="104" y="134" fill="#222">Title Goes</text><text x="104" y="144" fill="#222">Here!</text>
    <text x="222" y="134" fill="var(--teal)">Title Goes</text><text x="222" y="144" fill="var(--teal)">Here!</text>
    <text x="340" y="134" fill="#222">Title Goes</text><text x="340" y="144" fill="#222">Here!</text>
    <text x="458" y="134" fill="#222">Title Goes</text><text x="458" y="144" fill="#222">Here!</text>
  </g>
  <g class="b" font-size="5.6" fill="#555" text-anchor="middle">
    <text x="104" y="157">Lorem ipsum dolor</text><text x="104" y="164">sit amet, consectetur</text><text x="104" y="171">adipiscing elit.</text><text x="104" y="178">Vivamus eu dui ex.</text><text x="104" y="185">Curabitur.</text>
    <text x="222" y="157">Lorem ipsum dolor</text><text x="222" y="164">sit amet, consectetur</text><text x="222" y="171">adipiscing elit.</text><text x="222" y="178">Vivamus eu dui ex.</text><text x="222" y="185">Curabitur.</text>
    <text x="340" y="157">Lorem ipsum dolor</text><text x="340" y="164">sit amet, consectetur</text><text x="340" y="171">adipiscing elit.</text><text x="340" y="178">Vivamus eu dui ex.</text><text x="340" y="185">Curabitur.</text>
    <text x="458" y="157">Lorem ipsum dolor</text><text x="458" y="164">sit amet, consectetur</text><text x="458" y="171">adipiscing elit.</text><text x="458" y="178">Vivamus eu dui ex.</text><text x="458" y="185">Curabitur.</text>
  </g>
  <path d="M0 276H70L94 302H563V304H92L69 279H0Z" fill="var(--teal)"/>
  <path d="M0 279H69L92 304H0Z" fill="var(--teal)"/>
  <path d="M0 304H563V307H0Z" fill="var(--navy)"/>
  <text class="brand" x="8" y="295" font-size="7" fill="#fff">Adrien Valcourt</text>
  <text class="b" x="530" y="300" font-size="4.5" fill="#444" text-anchor="end">Copyright 2021 Adrien Valcourt. All rights reserved  |</text>
  <text class="b" x="545" y="300" font-size="5" fill="#444" text-anchor="end">9</text>
</svg></div>

<!-- Three boxes -->
<div class="slide c2 r5"><svg viewBox="0 0 563 316">
  <defs><linearGradient id="b10" x1="0" y1="0" x2="1" y2="0"><stop offset="0" stop-color="#0e8391"/><stop offset="1" stop-color="#0b5f73"/></linearGradient></defs>
  <rect width="563" height="120" fill="url(#b10)" role="img" aria-label="Photo of a meeting, tinted teal"/>
  <text class="hm" x="33" y="48" font-size="22" fill="#fff">Slide Title <tspan class="hl">Goes Here!</tspan></text>
  <line x1="33" y1="58" x2="280" y2="58" stroke="#fff" stroke-width="1"/>
  <rect x="50" y="88" width="136" height="140" rx="6" fill="var(--navy)" stroke="#fff" stroke-width="2"/>
  <rect x="209" y="88" width="136" height="140" rx="6" fill="var(--teal)" stroke="#fff" stroke-width="2"/>
  <rect x="368" y="88" width="136" height="140" rx="6" fill="var(--grey)" stroke="#fff" stroke-width="2"/>
  <g class="b" font-size="6.3" fill="#fff">
    <g transform="translate(60 0)">
      <circle cx="3" cy="102" r="1.3"/><text x="9" y="104">Lorem ipsum dolor sit amet,</text><text x="9" y="111">consectetur adipiscing elit.</text><text x="9" y="118">Vivamus eu dui ex.</text>
      <circle cx="3" cy="133" r="1.3"/><text x="9" y="135">Curabitur dapibus dignissim</text><text x="9" y="142">dui, in molestie metus</text><text x="9" y="149">feugiat sed.</text>
      <circle cx="3" cy="164" r="1.3"/><text x="9" y="166">Praesent aliquet lorem ex,</text><text x="9" y="173">eu dapibus odio varius at.</text>
      <circle cx="3" cy="188" r="1.3"/><text x="9" y="190">Duis eget tellus porta,</text><text x="9" y="197">consequat lacus vitae,</text><text x="9" y="204">venenatis dolor.</text>
    </g>
    <g transform="translate(219 0)">
      <circle cx="3" cy="102" r="1.3"/><text x="9" y="104">Lorem ipsum dolor sit amet,</text><text x="9" y="111">consectetur adipiscing elit.</text><text x="9" y="118">Vivamus eu dui ex.</text>
      <circle cx="3" cy="133" r="1.3"/><text x="9" y="135">Curabitur dapibus dignissim</text><text x="9" y="142">dui, in molestie metus</text><text x="9" y="149">feugiat sed.</text>
      <circle cx="3" cy="164" r="1.3"/><text x="9" y="166">Praesent aliquet lorem ex,</text><text x="9" y="173">eu dapibus odio varius at.</text>
      <circle cx="3" cy="188" r="1.3"/><text x="9" y="190">Duis eget tellus porta,</text><text x="9" y="197">consequat lacus vitae,</text><text x="9" y="204">venenatis dolor.</text>
    </g>
    <g transform="translate(378 0)">
      <circle cx="3" cy="102" r="1.3"/><text x="9" y="104">Lorem ipsum dolor sit amet,</text><text x="9" y="111">consectetur adipiscing elit.</text><text x="9" y="118">Vivamus eu dui ex.</text>
      <circle cx="3" cy="133" r="1.3"/><text x="9" y="135">Curabitur dapibus dignissim</text><text x="9" y="142">dui, in molestie metus</text><text x="9" y="149">feugiat sed.</text>
      <circle cx="3" cy="164" r="1.3"/><text x="9" y="166">Praesent aliquet lorem ex,</text><text x="9" y="173">eu dapibus odio varius at.</text>
      <circle cx="3" cy="188" r="1.3"/><text x="9" y="190">Duis eget tellus porta,</text><text x="9" y="197">consequat lacus vitae,</text><text x="9" y="204">venenatis dolor.</text>
    </g>
  </g>
  <g class="b" font-size="13" text-anchor="middle">
    <text x="118" y="250" fill="var(--navy)">Heading 1</text>
    <text x="277" y="250" fill="var(--teal)">Heading 2</text>
    <text x="436" y="250" fill="var(--grey)">Heading 3</text>
  </g>
  <path d="M0 276H70L94 302H563V304H92L69 279H0Z" fill="var(--teal)"/>
  <path d="M0 279H69L92 304H0Z" fill="var(--teal)"/>
  <path d="M0 304H563V307H0Z" fill="var(--navy)"/>
  <text class="brand" x="8" y="295" font-size="7" fill="#fff">Adrien Valcourt</text>
  <text class="b" x="530" y="300" font-size="4.5" fill="#444" text-anchor="end">Copyright 2021 Adrien Valcourt. All rights reserved  |</text>
  <text class="b" x="545" y="300" font-size="5" fill="#444" text-anchor="end">10</text>
</svg></div>

<!-- Section break light -->
<div class="slide c1 r6"><svg viewBox="0 0 563 316">
  <defs><linearGradient id="s11" x1="0" y1="0" x2="1" y2="1"><stop offset="0" stop-color="#f7f8f8"/><stop offset="1" stop-color="#e3e7e8"/></linearGradient></defs>
  <rect width="563" height="316" fill="url(#s11)" role="img" aria-label="Faded overhead photo of people working at a desk"/>
  <text class="brand" x="45" y="150" font-size="16" fill="var(--teal)">Adrien Valcourt</text>
  <text class="h" x="45" y="210" font-size="32" fill="var(--navy)">Section Break</text>
  <text class="b" x="45" y="240" font-size="14" fill="var(--teal)">Subtitle of Section Break Goes Here!</text>
</svg></div>

<!-- Column chart + table -->
<div class="slide c2 r6"><svg viewBox="0 0 563 316">
  <text class="hm" x="33" y="48" font-size="22" fill="var(--teal)">Slide Title <tspan class="hl">Goes Here!</tspan></text>
  <line x1="33" y1="58" x2="280" y2="58" stroke="var(--teal)" stroke-width="1"/>
  <g class="b" font-size="5" fill="#555" text-anchor="end">
    <text x="50" y="237">0</text><text x="50" y="215">1</text><text x="50" y="194">2</text><text x="50" y="172">3</text><text x="50" y="150">4</text><text x="50" y="129">5</text><text x="50" y="107">6</text>
  </g>
  <line x1="55" y1="235" x2="275" y2="235" stroke="#ccc" stroke-width="0.6"/>
  <g>
    <rect x="62" y="142" width="6" height="93" fill="var(--navy)"/><rect x="70" y="183" width="6" height="52" fill="var(--teal)"/><rect x="78" y="192" width="6" height="43" fill="var(--grey)"/>
    <rect x="98" y="181" width="6" height="54" fill="var(--navy)"/><rect x="106" y="140" width="6" height="95" fill="var(--teal)"/><rect x="114" y="192" width="6" height="43" fill="var(--grey)"/>
    <rect x="134" y="159" width="6" height="76" fill="var(--navy)"/><rect x="142" y="196" width="6" height="39" fill="var(--teal)"/><rect x="150" y="170" width="6" height="65" fill="var(--grey)"/>
    <rect x="170" y="137" width="6" height="98" fill="var(--navy)"/><rect x="178" y="174" width="6" height="61" fill="var(--teal)"/><rect x="186" y="126" width="6" height="109" fill="var(--grey)"/>
    <rect x="206" y="142" width="6" height="93" fill="var(--navy)"/><rect x="214" y="183" width="6" height="52" fill="var(--teal)"/><rect x="222" y="192" width="6" height="43" fill="var(--grey)"/>
    <rect x="242" y="181" width="6" height="54" fill="var(--navy)"/><rect x="250" y="140" width="6" height="95" fill="var(--teal)"/><rect x="258" y="192" width="6" height="43" fill="var(--grey)"/>
  </g>
  <g class="b" font-size="5" fill="#555" text-anchor="middle">
    <text x="73" y="244">Category 1</text><text x="109" y="244">Category 2</text><text x="145" y="244">Category 3</text><text x="181" y="244">Category 4</text><text x="217" y="244">Category 5</text><text x="253" y="244">Category 6</text>
  </g>
  <g class="b" font-size="6.3" fill="#444">
    <text x="289" y="98">Lorem ipsum dolor sit amet, at laborum nibh duis mauris. Per</text>
    <text x="289" y="106">ultrices lectus sed metus tristique eu. Diam suspendisse ac ipsum</text>
    <text x="289" y="114">maecenas fermentum, aliquet imperdiet et lobortis venenatis</text>
    <text x="289" y="122">nascetur lacus. A ac, vivamus erat nullam.</text>
  </g>
  <rect x="287" y="133" width="243" height="13" fill="var(--navy)"/>
  <g class="bs" font-size="6.5" fill="#fff"><text x="291" y="142">Category</text><text x="390" y="142">Series 1</text><text x="439" y="142">Series 2</text><text x="488" y="142">Series 3</text></g>
  <g stroke="#ddd" stroke-width="0.5"><line x1="287" y1="160" x2="530" y2="160"/><line x1="287" y1="174" x2="530" y2="174"/><line x1="287" y1="188" x2="530" y2="188"/><line x1="287" y1="202" x2="530" y2="202"/><line x1="287" y1="216" x2="530" y2="216"/><line x1="287" y1="230" x2="530" y2="230"/></g>
  <g class="b" font-size="6" fill="#555">
    <text x="291" y="156">Category 1</text><text x="405" y="156">4.3</text><text x="455" y="156">2.4</text><text x="505" y="156">2</text>
    <text x="291" y="170">Category 2</text><text x="405" y="170">2.5</text><text x="455" y="170">4.4</text><text x="505" y="170">2</text>
    <text x="291" y="184">Category 3</text><text x="405" y="184">3.5</text><text x="455" y="184">1.8</text><text x="505" y="184">3</text>
    <text x="291" y="198">Category 4</text><text x="405" y="198">4.5</text><text x="455" y="198">2.8</text><text x="505" y="198">5</text>
    <text x="291" y="212">Category 5</text><text x="405" y="212">4.3</text><text x="455" y="212">2.4</text><text x="505" y="212">2</text>
    <text x="291" y="226">Category 6</text><text x="405" y="226">2.5</text><text x="455" y="226">4.4</text><text x="505" y="226">2</text>
  </g>
  <path d="M0 276H70L94 302H563V304H92L69 279H0Z" fill="var(--teal)"/>
  <path d="M0 279H69L92 304H0Z" fill="var(--teal)"/>
  <path d="M0 304H563V307H0Z" fill="var(--navy)"/>
  <text class="brand" x="8" y="295" font-size="7" fill="#fff">Adrien Valcourt</text>
  <text class="b" x="530" y="300" font-size="4.5" fill="#444" text-anchor="end">Copyright 2021 Adrien Valcourt. All rights reserved  |</text>
  <text class="b" x="545" y="300" font-size="5" fill="#444" text-anchor="end">12</text>
</svg></div>

<!-- Horizontal bar chart -->
<div class="slide c1 r7"><svg viewBox="0 0 563 316">
  <text class="hm" x="33" y="48" font-size="22" fill="var(--teal)">Slide Title Goes Here!</text>
  <line x1="33" y1="58" x2="280" y2="58" stroke="var(--teal)" stroke-width="1"/>
  <line x1="82" y1="95" x2="82" y2="232" stroke="#aaa" stroke-width="0.6"/>
  <g class="b" font-size="5" fill="#555" text-anchor="end">
    <text x="76" y="108">Category 4</text><text x="76" y="143">Category 3</text><text x="76" y="178">Category 2</text><text x="76" y="213">Category 1</text>
  </g>
  <g>
    <rect x="82" y="98" width="188" height="5" fill="var(--grey)"/><rect x="82" y="104" width="105" height="5" fill="var(--teal)"/><rect x="82" y="110" width="167" height="5" fill="var(--navy)"/>
    <rect x="82" y="133" width="113" height="5" fill="var(--grey)"/><rect x="82" y="139" width="68" height="5" fill="var(--teal)"/><rect x="82" y="145" width="132" height="5" fill="var(--navy)"/>
    <rect x="82" y="168" width="75" height="5" fill="var(--grey)"/><rect x="82" y="174" width="165" height="5" fill="var(--teal)"/><rect x="82" y="180" width="94" height="5" fill="var(--navy)"/>
    <rect x="82" y="203" width="75" height="5" fill="var(--grey)"/><rect x="82" y="209" width="90" height="5" fill="var(--teal)"/><rect x="82" y="215" width="162" height="5" fill="var(--navy)"/>
  </g>
  <g class="b" font-size="5" fill="#555" text-anchor="middle">
    <text x="82" y="242">0</text><text x="120" y="242">1</text><text x="157" y="242">2</text><text x="195" y="242">3</text><text x="232" y="242">4</text><text x="270" y="242">5</text><text x="307" y="242">6</text>
  </g>
  <line x1="322" y1="95" x2="322" y2="245" stroke="#ddd" stroke-width="0.6"/>
  <rect x="342" y="97" width="9" height="9" fill="var(--navy)"/>
  <rect x="342" y="152" width="9" height="9" fill="var(--teal)"/>
  <rect x="342" y="207" width="9" height="9" fill="var(--grey)"/>
  <g class="bs" font-size="9"><text x="362" y="105" fill="var(--navy)">Title Goes Here!</text><text x="362" y="160" fill="var(--teal)">Title Goes Here!</text><text x="362" y="215" fill="var(--grey)">Title Goes Here!</text></g>
  <g class="b" font-size="5.6" fill="#555">
    <text x="362" y="115">Lorem ipsum dolor sit amet, at laborum nibh</text><text x="362" y="122">duis mauris. Per ultrices lectus sed metus</text><text x="362" y="129">tristique eu. Diam suspendisse ac ipsum</text>
    <text x="362" y="170">Lorem ipsum dolor sit amet, at laborum nibh</text><text x="362" y="177">duis mauris. Per ultrices lectus sed metus</text><text x="362" y="184">tristique eu. Diam suspendisse ac ipsum</text>
    <text x="362" y="225">Lorem ipsum dolor sit amet, at laborum nibh</text><text x="362" y="232">duis mauris. Per ultrices lectus sed metus</text><text x="362" y="239">tristique eu. Diam suspendisse ac ipsum</text>
  </g>
  <path d="M0 276H70L94 302H563V304H92L69 279H0Z" fill="var(--teal)"/>
  <path d="M0 279H69L92 304H0Z" fill="var(--teal)"/>
  <path d="M0 304H563V307H0Z" fill="var(--navy)"/>
  <text class="brand" x="8" y="295" font-size="7" fill="#fff">Adrien Valcourt</text>
  <text class="b" x="530" y="300" font-size="4.5" fill="#444" text-anchor="end">Copyright 2021 Adrien Valcourt. All rights reserved  |</text>
  <text class="b" x="545" y="300" font-size="5" fill="#444" text-anchor="end">13</text>
</svg></div>

<!-- Donut charts -->
<div class="slide c2 r7"><svg viewBox="0 0 563 316">
  <text class="hm" x="33" y="48" font-size="22" fill="var(--teal)">Slide Title Goes Here!</text>
  <line x1="33" y1="58" x2="280" y2="58" stroke="var(--teal)" stroke-width="1"/>
  <g fill="none" stroke-width="5">
    <circle cx="125" cy="122" r="42" stroke="var(--navy)" stroke-dasharray="169 264" transform="rotate(-90 125 122)"/>
    <circle cx="281" cy="122" r="42" stroke="var(--teal)" stroke-dasharray="216 264" transform="rotate(-90 281 122)"/>
    <circle cx="437" cy="122" r="42" stroke="var(--grey)" stroke-dasharray="248 264" transform="rotate(-90 437 122)"/>
  </g>
  <g class="hl" font-size="22" text-anchor="middle">
    <text x="125" y="130" fill="var(--navy)">64<tspan font-size="14">%</tspan></text>
    <text x="281" y="130" fill="var(--teal)">82<tspan font-size="14">%</tspan></text>
    <text x="437" y="130" fill="var(--grey)">94<tspan font-size="14">%</tspan></text>
  </g>
  <g class="b" font-size="13" text-anchor="middle">
    <text x="125" y="189" fill="var(--navy)">Heading</text><text x="281" y="189" fill="var(--teal)">Heading</text><text x="437" y="189" fill="var(--grey)">Heading</text>
  </g>
  <g class="b" font-size="5.8" fill="#555" text-anchor="middle">
    <text x="125" y="201">Lorem ipsum dolor sit amet, at</text><text x="125" y="208">laborum nibh duis mauris. Per</text><text x="125" y="215">ultrices lectus sed metus.</text>
    <text x="281" y="201">Lorem ipsum dolor sit amet, at</text><text x="281" y="208">laborum nibh duis mauris. Per</text><text x="281" y="215">ultrices lectus sed metus.</text>
    <text x="437" y="201">Lorem ipsum dolor sit amet, at</text><text x="437" y="208">laborum nibh duis mauris. Per</text><text x="437" y="215">ultrices lectus sed metus.</text>
  </g>
  <path d="M0 276H70L94 302H563V304H92L69 279H0Z" fill="var(--teal)"/>
  <path d="M0 279H69L92 304H0Z" fill="var(--teal)"/>
  <path d="M0 304H563V307H0Z" fill="var(--navy)"/>
  <text class="brand" x="8" y="295" font-size="7" fill="#fff">Adrien Valcourt</text>
  <text class="b" x="530" y="300" font-size="4.5" fill="#444" text-anchor="end">Copyright 2021 Adrien Valcourt. All rights reserved  |</text>
  <text class="b" x="545" y="300" font-size="5" fill="#444" text-anchor="end">14</text>
</svg></div>

<!-- Contact -->
<div class="slide cc r8"><svg viewBox="0 0 563 316">
  <defs><linearGradient id="c15" x1="0" y1="0" x2="0" y2="1"><stop offset="0" stop-color="#0b5f73"/><stop offset="1" stop-color="#0e8a99"/></linearGradient></defs>
  <rect width="563" height="316" fill="url(#c15)" role="img" aria-label="Photo of a handshake, tinted teal"/>
  <text class="brand" x="196" y="160" font-size="16" fill="#fff" text-anchor="middle">Adrien Valcourt</text>
  <line x1="297" y1="115" x2="297" y2="205" stroke="#fff" stroke-opacity=".5" stroke-width="0.8"/>
  <text class="hm" x="315" y="128" font-size="11" fill="#fff">Contact Us</text>
  <g fill="#fff">
    <path d="M317 143c0 5 4 9 9 9l1.5-2-2.5-1.5-1.2 1c-1.5-.7-2.7-1.9-3.4-3.4l1-1.2-1.5-2.5z"/>
    <circle cx="322" cy="163" r="3.5" fill="none" stroke="#fff" stroke-width="1.3"/>
    <circle cx="322" cy="180" r="4.5" fill="none" stroke="#fff" stroke-width="1"/>
    <line x1="317.5" y1="180" x2="326.5" y2="180" stroke="#fff" stroke-width=".7"/>
  </g>
  <g class="b" font-size="8" fill="#fff">
    <text x="334" y="150">0100-555-0147</text>
    <text x="334" y="166">info@Adrien-Valcourt.com</text>
    <text x="334" y="183">www.Adrien-Valcourt.com</text>
  </g>
</svg></div>

</div>
</body>
</html>
```